Stonebay Towing Business Card

Towing
Accident towing
Mechanical breakdown
Insurance, salvage and recovery
4wd off road towing
Light & Heavy towing
8347 2516
24 hour business 7 days

Logo can be whole size on front

Industry/Entity Type

Towing/ transport

Contact Information for Business Card

The above

```html
<!DOCTYPE html>
<html lang="en">
<head>
<meta charset="utf-8">
<title>Stonebay Towing Business Card</title>
<link href="https://fonts.googleapis.com/css2?family=Roboto:wght@700;900&display=swap" rel="stylesheet">
<style>
  :root {
    --brand-red: #d71f27;
    --ink: #1a1a1a;
    --card: #ffffff;
    --backdrop: #e6e6e6;
  }
  * { box-sizing: border-box; margin: 0; padding: 0; }
  html, body { width: 1200px; height: 694px; overflow: hidden; }
  body {
    background: var(--backdrop);
    font-family: "Roboto", Arial, sans-serif;
    position: relative;
  }
  .card {
    position: absolute;
    top: 190px;
    width: 540px;
    height: 314px;
    background: var(--card);
    border-radius: 28px;
    box-shadow: 0 6px 18px rgba(0,0,0,0.18);
  }
  .card::before {
    content: "";
    position: absolute;
    inset: 14px;
    border: 3px solid var(--brand-red);
    border-radius: 20px;
    pointer-events: none;
  }
  .card-front { left: 30px; }
  .card-back { left: 630px; }

  .front-wordmark {
    position: absolute;
    inset: 0;
    display: flex;
    align-items: center;
    justify-content: center;
    color: var(--brand-red);
    font-weight: 900;
    font-size: 52px;
    letter-spacing: 0.5px;
  }

  .back-wordmark {
    position: absolute;
    top: 30px;
    right: 38px;
    color: var(--brand-red);
    font-weight: 900;
    font-size: 24px;
    line-height: 1;
  }
  .rule {
    position: absolute;
    left: 16px;
    right: 16px;
    height: 2px;
    background: var(--brand-red);
  }
  .rule-top { top: 68px; left: 300px; }
  .rule-bottom { top: 180px; }

  .hours {
    position: absolute;
    top: 34px;
    left: 40px;
    font-weight: 700;
    font-size: 15px;
    line-height: 1.2;
    color: var(--ink);
    text-transform: uppercase;
  }
  .phone-row {
    position: absolute;
    top: 92px;
    left: 40px;
    display: flex;
    align-items: center;
    gap: 18px;
  }
  .phone-icon { width: 40px; height: 40px; flex: none; }
  .phone-number {
    color: var(--brand-red);
    font-weight: 900;
    font-size: 58px;
    letter-spacing: 12px;
    line-height: 1;
    white-space: nowrap;
  }
  .services {
    position: absolute;
    list-style: none;
    font-weight: 700;
    font-size: 12px;
    line-height: 1.9;
    color: var(--ink);
    text-transform: uppercase;
    white-space: nowrap;
  }
  .services li::before {
    content: "";
    display: inline-block;
    width: 8px;
    height: 8px;
    border-radius: 50%;
    background: var(--brand-red);
    margin-right: 10px;
    vertical-align: 1px;
  }
  .services-main { top: 196px; left: 40px; }
  .services-extra { top: 196px; left: 262px; }
</style>
</head>
<body>
  <section class="card card-front">
    <div class="front-wordmark">Stonebay Towing</div>
  </section>

  <section class="card card-back">
    <p class="hours">24 Hour Business<br>and 7 Days</p>
    <div class="back-wordmark">Stonebay Towing</div>
    <div class="rule rule-top"></div>

    <div class="phone-row">
      <svg class="phone-icon" viewBox="0 0 40 40" aria-hidden="true">
        <path d="M8 18c-1-3 1-6 4-7l3 6-3 2c1 3 4 6 7 7l2-3 6 3c-1 3-4 5-7 4C14 29 10 24 8 18z" fill="#1a1a1a"/>
        <path d="M22 10a8 8 0 0 1 8 8" stroke="#1a1a1a" stroke-width="2" fill="none" stroke-linecap="round"/>
        <path d="M22 5a13 13 0 0 1 13 13" stroke="#1a1a1a" stroke-width="2" fill="none" stroke-linecap="round"/>
      </svg>
      <span class="phone-number">8347 2516</span>
    </div>

    <div class="rule rule-bottom"></div>

    <ul class="services services-main">
      <li>Towing</li>
      <li>Accident Towing</li>
      <li>Mechanical Breakdown</li>
    </ul>

    <ul class="services services-extra">
      <li>Insurance, Salvage and Recovery</li>
      <li>4WD Off Road Towing</li>
      <li>Light &amp; Heavy Towing</li>
    </ul>
  </section>
</body>
</html>
```